Halloween Style Website Design

We need a website design with a Halloween theme.

I have provided 3 wireframes to work from. If you like you can just design the homepage first. If we like your designs we will instruct you to design the other pages once we narrow them down.

The website will be totally halloween themed. We will use vector type designs.

We want a feel similar to this style I guess:

https://v.clipvarn.net/pic/Kt7mQ2wLx9aR/largestill.jpg
https://media.sketchlorn.com/members/5172804/captures/3318467/panel_2__2_.jpg
https://img4.plotmerrow.com/p/1000x1000/41/09/halloween-castle-background-design-vector-58301746.jpg
https://pix.graventa.com/free-vector/decorative-halloween-background-flat-style_48-7715302946.jpg?size=626&ext=jpg
https://bx7.quillomedia.net/jpg/05/31/96/48/500_K_531964827_rTmWbZeLoNcYpQ4sVhGaJdKiUvXyFe2s.jpg

```html
<!DOCTYPE html>
<html lang="en">
<head>
<meta charset="utf-8">
<title>My Trick Or Treat</title>
<link href="https://fonts.googleapis.com/css2?family=Montserrat:wght@400;500;700;800&display=swap" rel="stylesheet">
<style>
  :root {
    --navy-deep: #08134a;
    --navy: #0b1c66;
    --card-bg: #0a195c;
    --footer-bar: #0b2385;
    --cyan: #2ff0f4;
    --purple: #7a4cff;
    --white: #ffffff;
    --muted: #c9cde6;
    --art-night: #1a2766;
    --art-green: #4f8a3a;
    --art-teal: #157f96;
    --art-amber: #d9a53c;
  }
  * { margin: 0; padding: 0; box-sizing: border-box; }
  html, body { width: 856px; height: 1200px; overflow: hidden; }
  body {
    position: relative;
    font-family: 'Montserrat', sans-serif;
    color: var(--white);
    background: linear-gradient(180deg, #061a6a 0%, #0a1b63 30%, #0a1756 60%, #08134a 100%);
  }
  .abs { position: absolute; }

  .site-header {
    position: absolute; left: 0; top: 0; width: 856px; height: 57px;
    background: linear-gradient(90deg, #0a1447 0%, #0b1a5c 60%, #0b1f78 100%);
  }
  .logo { left: 106px; top: 17px; font-size: 19px; font-weight: 800; color: var(--cyan); letter-spacing: 0.5px; }
  .nav-link { top: 22px; font-size: 9.6px; font-weight: 700; color: var(--white); text-decoration: none; }
  .nav-link.is-active { color: var(--cyan); }

  .btn {
    position: absolute; display: flex; align-items: center; justify-content: center;
    border-radius: 4px; font-weight: 700; color: var(--white); text-decoration: none;
    background: linear-gradient(90deg, var(--purple) 0%, #5b8cff 55%, var(--cyan) 100%);
  }
  .btn-header { left: 663px; top: 16px; width: 86px; height: 25px; font-size: 9.6px; }

  .hero-art {
    left: 60px; top: 78px; width: 276px; height: 214px; border-radius: 12px;
    background: linear-gradient(160deg, var(--art-night) 0%, var(--art-green) 60%, #b9b44a 100%);
  }
  .hero-title { left: 361px; top: 105px; font-size: 19.5px; font-weight: 800; color: var(--cyan); white-space: nowrap; }
  .hero-text { left: 361px; top: 141px; width: 396px; font-size: 7.55px; line-height: 13.9px; font-weight: 500; }
  .btn-learn { left: 644px; top: 259px; width: 85px; height: 25px; font-size: 9.6px; }
  .learn-arrow { left: 734px; top: 268px; }

  .feature-card {
    position: absolute; top: 347px; width: 194px; height: 222px; border-radius: 4px;
    padding: 2px;
    background: linear-gradient(180deg, var(--purple) 0%, var(--cyan) 100%);
  }
  .feature-card .inner {
    width: 100%; height: 100%; border-radius: 3px; background: var(--card-bg);
    padding: 17px 8px 0 18px;
  }
  .feature-card h2 { text-align: center; font-size: 19.5px; font-weight: 800; margin: 0 10px 12px 0; }
  .feature-card p { font-size: 7.5px; line-height: 13.9px; font-weight: 500; }

  .signup-panel {
    position: absolute; left: 108px; top: 621px; width: 641px; height: 88px; border-radius: 4px; padding: 2px;
    background: linear-gradient(180deg, var(--purple) 0%, var(--cyan) 100%);
  }
  .signup-panel .inner { position: relative; width: 100%; height: 100%; border-radius: 3px; background: #09185a; }
  .signup-title { left: 19px; top: 28px; font-size: 20px; font-weight: 800; }
  .signup-text { left: 126px; top: 23px; width: 370px; font-size: 7.6px; line-height: 13.9px; font-weight: 500; }
  .btn-signup { left: 531px; top: 30px; width: 85px; height: 25px; font-size: 9.6px; }

  .scene-art {
    left: 107px; top: 760px; width: 642px; height: 262px; border-radius: 6px;
    background: linear-gradient(90deg, #0f3f6e 0%, var(--art-teal) 50%, var(--art-amber) 100%);
  }

  .footer-line {
    left: 0; top: 1100px; width: 856px; height: 1px;
    background: linear-gradient(90deg, var(--cyan) 0%, var(--purple) 100%);
  }
  .footer-link { top: 1131px; font-size: 10px; font-weight: 400; color: var(--white); text-decoration: none; }
  .copyright-bar {
    left: 0; top: 1174px; width: 856px; height: 26px; background: var(--footer-bar);
    display: flex; align-items: center; justify-content: center;
    font-size: 7.5px; color: var(--muted);
  }
  .copyright-bar a { color: var(--muted); }
</style>
</head>
<body>
  <header class="site-header">
    <div class="abs logo">LOGO</div>
    <nav>
      <a class="abs nav-link" style="left:320px" href="#">Home</a>
      <a class="abs nav-link" style="left:383px" href="#">Build</a>
      <a class="abs nav-link is-active" style="left:442px" href="#">Tricks</a>
      <a class="abs nav-link" style="left:504px" href="#">Treats</a>
      <a class="abs nav-link" style="left:612px;top:21px" href="#">Login</a>
    </nav>
    <a class="btn btn-header" href="#">Sign Up</a>
  </header>

  <div class="abs hero-art" role="img" aria-label="Cartoon monster kid with ghosts and bats under bare trees"></div>
  <h1 class="abs hero-title">Welcome to My Trick Or Treat!</h1>
  <p class="abs hero-text">Lorem ipsum dolor sit amet, consectetur adipiscing elit, sed do eiusmod tempor incididunt ut labore et dolore magna aliqua. Sed turpis tincidunt id aliquet risus feugiat in ante. Egestas congue quisque egestas diam in arcu cursus. Eget arcu dictum varius duis. Lacus vestibulum sed arcu non odio. Semper risus in hendrerit gravida rutrum quisque non tellus orci. Amet luctus venenatis lectus magna fringilla urna porttitor rhoncus dolor. Magnis dis parturient montes nascetur. Ut tellus elementum sagittis vitae et leo duis ut aliquet risus feugiat in ante vestibulum.</p>
  <a class="btn btn-learn" href="#">Learn More</a>
  <svg class="abs learn-arrow" width="14" height="16" viewBox="0 0 14 16" aria-hidden="true">
    <path d="M2 6 C2 2 12 1 12 6 C12 9 8 10 6 9" fill="none" stroke="#2ff0f4" stroke-width="2.2" stroke-linecap="round"/>
    <path d="M5 8 L7 15 L11 10 Z" fill="#2ff0f4"/>
  </svg>

  <section>
    <div class="feature-card" style="left:108px"><div class="inner">
      <h2>Build</h2>
      <p>Tempor commodo ullamcorper a lacus vestibulum. Volutpat odio facilisis mauris sit amet. Nisi porta lorem mollis aliquam. Platea dictumst quisque sagittis purus sit amet volutpat consequat. Pharetra magna ac placerat vestibulum lectus mauris ultrices eros in. At urna condimentum mattis cursus.</p>
    </div></div>
    <div class="feature-card" style="left:332px"><div class="inner">
      <h2>Tricks</h2>
      <p>Tempor commodo ullamcorper a lacus vestibulum. Volutpat odio facilisis mauris sit amet. Nisi porta lorem mollis aliquam. Platea dictumst quisque sagittis purus sit amet volutpat consequat. Pharetra magna ac placerat vestibulum lectus mauris ultrices eros in. At urna condimentum mattis cursus.</p>
    </div></div>
    <div class="feature-card" style="left:555px"><div class="inner">
      <h2>Treats</h2>
      <p>Tempor commodo ullamcorper a lacus vestibulum. Volutpat odio facilisis mauris sit amet. Nisi porta lorem mollis aliquam. Platea dictumst quisque sagittis purus sit amet volutpat consequat. Pharetra magna ac placerat vestibulum lectus mauris ultrices eros in. At urna condimentum mattis cursus.</p>
    </div></div>
  </section>

  <section class="signup-panel"><div class="inner">
    <h2 class="abs signup-title">Sign Up</h2>
    <p class="abs signup-text">Lorem ipsum dolor sit amet, consectetur adipiscing elit, sed do eiusmod tempor incididunt ut labore et dolore magna aliqua. Quis ipsum suspendisse ultrices gravida. Risus commodo viverra maecenas accumsan lacus vel facilisis. Pharetra magna ac placerat vestibulum.</p>
    <a class="btn btn-signup" href="#">Sign Up</a>
  </div></section>

  <div class="abs scene-art" role="img" aria-label="Halloween night landscape with a haunted castle, jack-o'-lantern, gravestone and full moon"></div>

  <footer>
    <div class="abs footer-line"></div>
    <a class="abs footer-link" style="left:263px" href="#">Home</a>
    <a class="abs footer-link" style="left:323px" href="#">Build</a>
    <a class="abs footer-link" style="left:379px" href="#">Tricks</a>
    <a class="abs footer-link" style="left:436px" href="#">Treats</a>
    <a class="abs footer-link" style="left:496px" href="#">Login</a>
    <a class="abs footer-link" style="left:553px" href="#">Sign Up</a>
    <div class="abs copyright-bar">Copyright © 2020 - My Trick Or Treat -&nbsp;<a href="#">Privacy Policy</a></div>
  </footer>
</body>
</html>
```